Commercial Cleaning Company Website Design

We are working with Harbor Sweep Team. They are a commercial cleaning company that needs a new website design.

Some sites to use for inspiration:

https://www.plenvask.com
https://glint-panecleaning.com
https://tidyhelpers.net
https://calmnesthouse.com
https://www.thecleaningbureauxyz.com
https://www.dottiebroom.com

Thank you for taking the time to consider designing a website for us. We are web developers based in Stockton and Los Angeles, CA, USA. Most of our projects go through the same process. Understanding this process may help you win a project with us. We custom-code all of our websites in-house. We don’t have any requirements as to what tools you use for your design, but we prefer Figma files. For any design that we label as four-stars, we send it to the client for review. The client picks the final design they want us to use. Once we complete this process, we will continue to show additional clients all the four-star sites and purchase them later. Your designs will have multiple chances to sell. For better chances of success, we ask that you follow these guidelines.

IMAGES:
If you use any images or icons in the design, we ask that you have a link to the asset so we can purchase the image/icon. Most of the designs we submit do not have the customer’s images on them unless they have some great images. Be creative; show us the feeling you are trying to portray with your image choices. Use any royalty-free site you choose. We subscribe to Adobe and mainly use their images, but we can purchase images outside of Adobe.

PLEASE NOTE: we will not submit designs to clients with watermarks on the images.

FONTS:
We ask that you identify the fonts used in the design. This can be done in a message if you want. We typically use Google Fonts and Adobe Fonts.

CONTENT:
We're always open to different content and ideas. We often submit designs with stock images so the client can see our vision. We typically take pictures after the website launch to use their images with our vision. Lorem Ipsum is fine for paragraphs, but we ask that you write the headers in correct English. We want to be able to show the vision and identify the sections of the website.

INSPIRATION:
We typically add a couple of links in the brief of websites we like to help you get started in your design.

REVISIONS:
We do not often ask for revisions of the designs unless we see something in the design that may not appeal to the client. If there are slight changes that we want to make, we do that in the development process.

FEEDBACK:
We rarely give feedback on designs during the design process. We are working on many website projects and do not have the time to provide feedback. We usually respond if your request is well thought out and asks specific questions, but a note asking “feedback, please” usually goes unanswered.

```html
<!DOCTYPE html>
<html lang="en">
<head>
<meta charset="utf-8">
<title>Harbor Sweep Team — Commercial Cleaning</title>
<link rel="stylesheet" href="https://fonts.googleapis.com/css2?family=Outfit:wght@400;500;600;700;800&display=swap">
<style>
:root{
  --orange:#f4511e;
  --yellow:#ffb000;
  --cream:#fff5e3;
  --blue:#1f52cc;
  --blue-deep:#1a45b3;
  --ink:#141414;
  --text:#333;
  --muted:#666;
  --dark:#1c1c1c;
  --field:#ececec;
}
*{box-sizing:border-box;margin:0;padding:0}
html,body{width:1200px;height:4640px;overflow:hidden}
body{font-family:"Outfit",sans-serif;color:var(--text);background:#fff;position:relative}
.abs{position:absolute}
.btn{position:absolute;display:flex;align-items:center;justify-content:center;border-radius:30px;color:#fff;font-weight:700;font-size:12px;letter-spacing:.3px;text-transform:uppercase}
.btn-orange{background:var(--orange)}
.btn-yellow{background:var(--yellow)}
.hl{color:var(--yellow)}
.photo{position:absolute;overflow:hidden}
.eyebrow{position:absolute;color:var(--orange);font-weight:600;font-size:13px;text-transform:uppercase}
.h2{position:absolute;font-weight:800;color:var(--ink);text-transform:uppercase;font-size:31px;line-height:1.15}

/* header & hero */
.hero{position:absolute;left:0;top:0;width:1200px;height:760px;background:linear-gradient(100deg,#8a3212 0%,#b9501d 35%,#c9743c 60%,#a8714c 100%)}
.brand{position:absolute;left:95px;top:28px;display:flex;align-items:center;gap:10px;color:#fff;font-weight:700;font-size:18px;letter-spacing:2px;text-transform:uppercase}
.brand .dot{width:14px;height:14px;border-radius:50%;background:var(--orange)}
.nav{position:absolute;top:34px;left:628px;display:flex;gap:22px;font-size:12px;color:#fff}
.hero-title{position:absolute;left:121px;top:198px;color:#fff;font-weight:800;font-size:46px;line-height:1.05;text-transform:uppercase}
.hero-copy{position:absolute;left:122px;top:365px;width:420px;color:#fff;font-size:12px;line-height:1.6}

/* why us */
.sheet{position:absolute;left:0;top:693px;width:1200px;height:1200px;background:#fff;border-radius:80px 80px 0 0}
.why{position:absolute;left:61px;top:768px;width:1077px;height:437px;background:var(--cream);border-radius:70px}
.why-copy{position:absolute;left:496px;top:130px;width:500px;font-size:12.5px;line-height:1.75}
.feature{position:absolute;top:297px;display:flex;align-items:center;gap:14px}
.feature .ic{width:64px;height:64px;border-radius:50%;display:flex;align-items:center;justify-content:center}
.feature b{display:block;font-size:9.5px;color:var(--ink);text-transform:uppercase;margin-bottom:4px}
.feature span{display:block;font-size:9.5px;line-height:1.4;width:120px;color:var(--muted)}

/* services */
.center{position:absolute;left:0;width:1200px;text-align:center}
.card{position:absolute;top:1390px;height:305px;background:#fff;border-radius:22px;box-shadow:0 8px 26px rgba(0,0,0,.09)}
.card .img{position:absolute;left:12px;right:12px;top:12px;height:162px;border-radius:4px}
.card h3{position:absolute;left:26px;top:200px;font-size:11px;font-weight:700;text-transform:uppercase;color:var(--ink)}
.card p{position:absolute;left:26px;top:222px;width:190px;font-size:9.5px;line-height:1.65;color:var(--muted)}
.card.active{background:var(--yellow)}
.card.active h3,.card.active p{color:#fff}
.card .go{position:absolute;right:38px;bottom:-18px;width:38px;height:38px;border-radius:50%;background:var(--orange);display:flex;align-items:center;justify-content:center}

/* industries */
.industries{position:absolute;left:0;top:1870px;width:1200px;height:680px;background:linear-gradient(135deg,var(--blue) 0%,var(--blue-deep) 100%);border-radius:0 90px 0 0}
.ind-list{position:absolute;top:315px;display:grid;grid-template-columns:193px 200px;row-gap:14px;font-size:12px;color:#fff}
.ind-list a{color:#fff;text-decoration:underline;display:flex;align-items:center;gap:8px}
.ind-list a::before{content:"";width:5px;height:5px;border-radius:50%;background:var(--orange)}

/* about */
.about-sheet{position:absolute;left:0;top:2472px;width:1200px;height:1700px;background:#fff;border-radius:90px 0 0 0}
.body-copy{position:absolute;font-size:11.5px;line-height:1.7;color:var(--text)}

/* cta */
.footer-band{position:absolute;left:0;top:4078px;width:1200px;height:562px;background:var(--dark);border-radius:80px 80px 0 0}
.cta{position:absolute;left:121px;top:3655px;width:957px;height:535px;background:var(--cream);border:2px solid var(--yellow);border-radius:70px}
.form{position:absolute;left:496px;top:97px;width:385px;height:333px;background:#fff;border-radius:30px;box-shadow:0 6px 24px rgba(0,0,0,.06)}
.field{position:absolute;left:40px;width:305px;height:44px;border-radius:10px;background:var(--field);font-size:13px;color:#888;padding:14px 26px}

/* footer */
.f-title{position:absolute;top:4300px;color:#fff;font-weight:700;font-size:16px;text-transform:uppercase}
.f-links{position:absolute;left:402px;top:4347px;list-style:none;font-size:11.5px;color:#ddd}
.f-links li{height:31px;display:flex;gap:8px}
.f-links li::before{content:"›";color:var(--orange)}
.f-contact{position:absolute;left:581px;font-size:11.5px;color:#ddd;line-height:1.5;display:flex;gap:10px}
.social{position:absolute;top:4418px;width:44px;height:44px;border-radius:50%;border:1px solid #555}
</style>
</head>
<body>

<!-- HERO -->
<section class="hero">
  <div class="photo" role="img" aria-label="Smiling cleaner in overalls and yellow gloves beside a cart of cleaning supplies" style="left:0;top:0;width:1200px;height:760px;background:linear-gradient(90deg,rgba(90,30,10,.55) 0%,rgba(0,0,0,0) 55%)"></div>
  <div class="brand"><span class="dot"></span>Harbor Sweep Team</div>
  <nav class="nav"><span>Home</span><span>About</span><span>Services</span><span>Industries</span><span>Reviews</span></nav>
  <div class="btn btn-orange" style="left:952px;top:22px;width:148px;height:40px">Get a Quote</div>
  <h1 class="hero-title">Sparkling Clean.<br>Every Time.<br><span class="hl">Guaranteed.</span></h1>
  <p class="hero-copy">From offices and schools to medical facilities and retail spaces — Harbor Sweep Team delivers a spotless, healthy environment your team and customers can trust.</p>
  <div class="btn btn-orange" style="left:122px;top:442px;width:148px;height:40px">Request a Quote</div>
  <div class="btn btn-yellow" style="left:302px;top:442px;width:134px;height:40px">Learn More</div>
</section>

<div class="sheet"></div>

<!-- WHY US -->
<section class="why">
  <div class="eyebrow" style="left:87px;top:88px">Why Choose Us</div>
  <h2 class="h2" style="left:87px;top:118px">Your Clean Space<br>Starts With <span class="hl">Harbor</span><br><span class="hl">Standards</span></h2>
  <p class="why-copy">At Harbor Sweep Team, we combine advanced cleaning technology, eco-friendly products, and highly trained staff to deliver exceptional commercial cleaning results. Whether it's a small office or a large facility, our team ensures every surface shines — safely, efficiently, and consistently.</p>
  <div class="feature" style="left:87px"><div class="ic" style="background:var(--orange)"><svg width="30" height="30" viewBox="0 0 24 24" fill="none" stroke="#fff" stroke-width="1.6"><circle cx="8" cy="8" r="3"/><circle cx="16" cy="8" r="3"/><path d="M2 20c0-4 3-6 6-6s6 2 6 6M10 20c0-4 3-6 6-6s6 2 6 6"/></svg></div><div><b>Professional Staff</b><span>Experienced, trained, and background-checked.</span></div></div>
  <div class="feature" style="left:319px"><div class="ic" style="background:var(--yellow)"><svg width="30" height="30" viewBox="0 0 24 24" fill="none" stroke="#fff" stroke-width="1.6"><path d="M5 19c0-8 6-13 15-14-1 9-6 15-14 15z"/><path d="M5 19l8-8"/></svg></div><div><b>Eco-Friendly Products</b><span>Safe for your employees and the planet.</span></div></div>
  <div class="feature" style="left:562px"><div class="ic" style="background:var(--orange)"><svg width="30" height="30" viewBox="0 0 24 24" fill="none" stroke="#fff" stroke-width="1.6"><circle cx="12" cy="12" r="9"/><path d="M12 7v5l3 3"/></svg></div><div><b>Flexible Scheduling</b><span>Daily, weekly, or custom cleaning plans.</span></div></div>
  <div class="feature" style="left:791px"><div class="ic" style="background:var(--orange)"><svg width="30" height="30" viewBox="0 0 24 24" fill="none" stroke="#fff" stroke-width="1.6"><path d="M4 21V9l8-5 8 5v12"/><path d="M9 21v-7h6v7M8 10h8"/></svg></div><div><b>Any Size Facility</b><span>From small offices to large corporate campuses.</span></div></div>
</section>

<!-- SERVICES -->
<h2 class="h2 center" style="top:1292px">Our Cleaning <span style="color:var(--yellow)">Services</span></h2>
<p class="center" style="top:1347px;font-size:12px">We tailor our cleaning services to fit your facility's unique needs. No job is too big or too small for our dedicated crew.</p>

<div class="card" style="left:94px;width:240px"><div class="img" role="img" aria-label="Cleaner vacuuming a modern office" style="background:linear-gradient(135deg,#b7c2c9,#6f7b84)"></div><h3>Office Cleaning</h3><p>Keep your workplace spotless &amp; productive with daily or scheduled cleaning.</p><div class="go"><svg width="12" height="12" viewBox="0 0 12 12" stroke="#fff" stroke-width="1.6" fill="none"><path d="M3 9l6-6M4 3h5v5"/></svg></div></div>
<div class="card" style="left:350px;width:230px"><div class="img" role="img" aria-label="Gloved hand spraying a glass window" style="background:linear-gradient(135deg,#cde3ef,#5d96c4)"></div><h3>Window &amp; Glass Cleaning</h3><p>Streak-free window cleaning for crystal-clear visibility and great first impressions.</p><div class="go"><svg width="12" height="12" viewBox="0 0 12 12" stroke="#fff" stroke-width="1.6" fill="none"><path d="M3 9l6-6M4 3h5v5"/></svg></div></div>
<div class="card active" style="left:606px;width:232px"><div class="img" role="img" aria-label="Yellow-gloved hands scrubbing a toilet" style="background:linear-gradient(135deg,#f4f4f4,#e9b23a)"></div><h3>Restroom Sanitization</h3><p>Deep cleaning and sanitization for healthy, odor-free restrooms.</p><div class="go"><svg width="12" height="12" viewBox="0 0 12 12" stroke="#fff" stroke-width="1.6" fill="none"><path d="M3 9l6-6M4 3h5v5"/></svg></div></div>
<div class="card" style="left:865px;width:241px"><div class="img" role="img" aria-label="Worker mopping a polished floor" style="background:linear-gradient(135deg,#9ea3a8,#4c5259)"></div><h3>Floor Care &amp; Maintenance</h3><p>Stripping, waxing, buffing, and carpet cleaning to protect and extend flooring life.</p><div class="go"><svg width="12" height="12" viewBox="0 0 12 12" stroke="#fff" stroke-width="1.6" fill="none"><path d="M3 9l6-6M4 3h5v5"/></svg></div></div>

<p class="center" style="top:1772px;font-size:11.5px;font-weight:600;color:var(--orange);text-decoration:underline">EXPLORE ALL SERVICES</p>

<!-- INDUSTRIES -->
<section class="industries">
  <div class="photo" role="img" aria-label="Healthcare cleaner pushing a cleaning trolley down a hospital corridor" style="left:162px;top:125px;width:403px;height:355px;border:3px solid #fff;border-radius:24px;background:linear-gradient(135deg,#e4e6e2,#a9b2b6)"></div>
  <h2 class="h2" style="left:626px;top:160px;color:#fff">Cleaning Solutions<br>For Every Industry</h2>
  <p class="abs" style="left:626px;top:247px;width:430px;font-size:11.5px;line-height:1.6;color:#fff">We proudly serve a wide range of industries — providing customized cleaning programs that meet each environment's standards and requirements.</p>
  <div class="ind-list" style="left:626px">
    <a>Corporate Offices</a><a>Gyms &amp; Fitness Centers</a>
    <a>Schools &amp; Universities</a><a>Government Buildings</a>
    <a>Healthcare Facilities</a><a>Industrial &amp; Warehouse Facilities</a>
    <a>Retail Stores</a>
  </div>
</section>

<!-- ABOUT -->
<div class="about-sheet"></div>
<div class="eyebrow" style="left:173px;top:2645px">About Us</div>
<h2 class="h2" style="left:173px;top:2673px">Your Trusted<br><span class="hl">Cleaning</span> Partner</h2>
<p class="body-copy" style="left:173px;top:2760px;width:375px">At Harbor Sweep Team, we believe a clean space is the foundation of a healthy and productive environment. Built on the values of reliability, integrity, and consistent quality, we've earned the confidence of businesses across the region.</p>
<p class="body-copy" style="left:173px;top:2845px;width:392px">Our dedicated team approaches every job with Harbor-level precision and pride — ensuring every corner, surface, and detail shines. From small offices to large facilities, we're more than just cleaners — we're partners in maintaining spaces that inspire trust and comfort.</p>
<div class="btn btn-orange" style="left:173px;top:2942px;width:157px;height:37px">Meet Our Team</div>
<div class="abs" style="left:837px;top:2578px;width:217px;height:247px;background:var(--orange);border-radius:40px"></div>
<div class="photo" role="img" aria-label="Three smiling cleaning crew members in overalls with a cleaning cart" style="left:665px;top:2627px;width:338px;height:425px;border-radius:30px;background:linear-gradient(160deg,#cfc6b8,#7e6f5e);box-shadow:0 10px 30px rgba(0,0,0,.15)"></div>

<!-- TESTIMONIAL -->
<div class="photo" role="img" aria-label="Two cleaners in aprons and yellow gloves holding supplies in a bright office" style="left:155px;top:3137px;width:443px;height:388px;border-radius:30px;background:linear-gradient(135deg,#eef0f0,#b8bdc0)"></div>
<div class="abs" style="left:562px;top:3420px;width:72px;height:36px;background:var(--yellow);border-radius:36px 36px 0 0"></div>
<svg class="abs" style="left:673px;top:3185px" width="56" height="46" viewBox="0 0 56 46"><path fill="#f4511e" d="M0 24C0 10 8 2 22 0l2 6C16 8 12 13 12 20h10v26H0zM32 24C32 10 40 2 54 0l2 6c-8 2-12 7-12 14h10v26H32z"/></svg>
<h2 class="h2" style="left:673px;top:3265px">What Our<br>Clients Are <span class="hl">Saying</span></h2>
<p class="body-copy" style="left:673px;top:3350px;width:360px">Harbor Sweep Team keeps our office spotless week after week. Their attention to detail is unmatched!</p>
<p class="abs" style="left:673px;top:3398px;font-size:11.5px;font-weight:700;color:var(--ink)">— DANA R., OFFICE MANAGER</p>
<svg class="abs" style="left:673px;top:3432px" width="92" height="16" viewBox="0 0 92 16" fill="#ffb000"><g id="s"><path d="M8 0l2.4 5 5.4.6-4 3.7 1.1 5.4L8 12l-4.9 2.7 1.1-5.4-4-3.7L5.6 5z"/></g><use href="#s" x="19"/><use href="#s" x="38"/><use href="#s" x="57"/><use href="#s" x="76"/></svg>

<!-- CTA -->
<div class="footer-band"></div>
<section class="cta">
  <h2 class="h2" style="left:92px;top:168px">Let's Get Your<br>Space <span class="hl">Sparkling!</span></h2>
  <p class="body-copy" style="left:92px;top:246px;width:330px;font-size:13px">Ready for a cleaner, healthier workplace? Contact Harbor Sweep Team today for a free quote and customized cleaning plan.</p>
  <div class="btn btn-orange" style="left:92px;top:333px;width:152px;height:40px">Get a Quote</div>
  <div class="form">
    <div class="field" style="top:46px">Name</div>
    <div class="field" style="top:100px">Email</div>
    <div class="field" style="top:153px">Phone</div>
    <div class="field" style="top:206px">Message / Cleaning Requirements</div>
    <div class="btn btn-orange" style="left:40px;top:260px;width:305px;height:44px;font-size:13px">Request a Free Quote</div>
  </div>
</section>

<!-- FOOTER -->
<div class="brand" style="top:4345px;font-size:20px"><span class="dot"></span>Harbor Sweep Team</div>
<div class="social" style="left:111px"></div>
<div class="social" style="left:165px"></div>
<div class="social" style="left:219px"></div>
<div class="social" style="left:273px"></div>

<div class="f-title" style="left:402px">Quick Links</div>
<ul class="f-links"><li>Home</li><li>About</li><li>Services</li><li>Industries</li><li>Reviews</li><li>Contact</li></ul>

<div class="f-title" style="left:581px">Contact Info</div>
<div class="f-contact" style="top:4332px"><svg width="14" height="12" viewBox="0 0 14 12"><rect width="14" height="11" rx="1.5" fill="#f4511e"/><path d="M1 1l6 5 6-5" stroke="#fff" fill="none"/></svg><span>Email:<br>info@harborsweepteam.com</span></div>
<div class="f-contact" style="top:4380px"><svg width="14" height="14" viewBox="0 0 24 24" fill="#f4511e"><path d="M6 2l4 5-2 3c1 3 3 5 6 6l3-2 5 4-2 4C10 22 2 14 2 4z"/></svg><span>Phone:<br>(555) 014-2270</span></div>
<div class="f-contact" style="top:4432px"><svg width="12" height="16" viewBox="0 0 12 16" fill="#f4511e"><path d="M6 0a6 6 0 016 6c0 4-6 10-6 10S0 10 0 6a6 6 0 016-6z"/><circle cx="6" cy="6" r="2" fill="#1c1c1c"/></svg><span>Location:<br>123 Main Street,<br>[Your City, State ZIP]</span></div>

<div class="f-title" style="left:845px">Newsletter</div>
<p class="abs" style="left:845px;top:4330px;width:200px;font-size:11.5px;line-height:1.5;color:#ddd">Subscribe to our email address to get the latest news.</p>
<div class="abs" style="left:845px;top:4352px;width:258px;height:45px;border-radius:24px;background:#2c2c2c;display:flex;align-items:center;padding:0 18px;gap:8px;font-size:12px;color:#ddd;justify-content:space-between;margin-top:20px">
  <span style="display:flex;gap:8px;align-items:center"><svg width="12" height="10" viewBox="0 0 14 12"><rect width="14" height="11" rx="1.5" fill="#f4511e"/></svg>Enter your email...</span>
  <svg width="16" height="16" viewBox="0 0 24 24" fill="#f4511e"><path d="M2 11L22 2l-9 20-2-8z"/></svg>
</div>

<div class="abs" style="left:1128px;top:4534px;width:44px;height:44px;border-radius:50%;background:var(--orange);display:flex;align-items:center;justify-content:center"><svg width="14" height="14" viewBox="0 0 14 14" stroke="#fff" stroke-width="1.8" fill="none"><path d="M7 12V2M3 6l4-4 4 4"/></svg></div>
<p class="center" style="top:4604px;font-size:11.5px;color:#ccc">© 2025 Harbor Sweep Team. All Rights Reserved.</p>

</body>
</html>
```